Quillo Stake Pool, redesign of existing website

Quillo is a stake pool that allow its users to stake their Tarnex crypto to yearn stable yields. The existing site is at www.quillostake.org The site is today is a little dull and I want to have suggestions for a redesign that makes the site stand out and that picks up the colors of the logo. I am not looking for a complete redesign, mainly colors and smaller changes to layout. Examples of sites to be inspired by www.vemba.network, https://app.toradel.finance/

Target Market(s)

Crypto users on Tarnex

Number of Pages Required

1 page

```html
<!DOCTYPE html>
<html lang="en">
<head>
<meta charset="utf-8">
<title>QuilloStake – Liquid Staking on Tarnex</title>
<link href="https://fonts.googleapis.com/css2?family=Inter:wght@400;500;600;700;800&display=swap" rel="stylesheet">
<style>
:root{
  --bg:#000000;
  --ink:#ffffff;
  --muted:#d7dde0;
  --accent:#1e9fc4;
  --teal:#0e9a94;
  --teal-deep:#0a5f60;
  --orange:#f47421;
  --card:#0b1213;
  --card-edge:#1a6b6a;
  --field:#1d2224;
  --field-edge:#8a9194;
  --pill:#175256;
  --pill-edge:#1f8f84;
  --tab:#1b2022;
  --footer:#06110f;
}
*{margin:0;padding:0;box-sizing:border-box}
html,body{width:1200px;height:720px;overflow:hidden;background:var(--bg);color:var(--ink);font-family:"Inter",sans-serif}
.page{position:relative;width:1200px;height:720px;overflow:hidden;background:radial-gradient(ellipse at 100% 0%,#0a2621 0%,rgba(0,0,0,0) 45%),var(--bg)}
.announce{position:absolute;top:0;left:0;width:1200px;height:23px;background:linear-gradient(90deg,#127f94,#0a9a73);font-size:9.5px;display:flex;align-items:center;justify-content:center;gap:3px}
.announce a{color:var(--ink);text-decoration:underline}
.nav{position:absolute;top:35px;left:184px;width:832px;height:34px;display:flex;align-items:center}
.brand{display:flex;align-items:center;gap:9px;font-weight:700;font-size:19px}
.brand-dot{width:22px;height:22px;border-radius:50%;background:var(--teal)}
.nav-links{margin-left:auto;display:flex;align-items:center;gap:22px;font-size:11px}
.nav-btn{background:#0d1111;border:1px solid #2a2f30;border-radius:5px;padding:8px 10px;font-weight:600;font-size:9.5px;margin-left:-1px}
.moon{position:absolute;left:8px;top:433px;width:1198px;height:1198px;border-radius:50%;background:radial-gradient(circle at 50% 30%,#1a8c88 0%,#137470 35%,#0f5f5c 60%,#0b4845 100%)}
.hero{position:absolute;left:184px;top:204px;width:400px}
.hero h1{font-size:40px;line-height:44px;font-weight:800;letter-spacing:-.3px}
.hero h1 span{color:var(--accent)}
.hero p{margin-top:20px;font-size:12px;line-height:21.3px;color:var(--muted)}
.hero-btn{position:absolute;top:188px;left:0;width:194px;height:42px;border:1px solid #2a2f30;border-radius:5px;background:#080a0a;display:flex;align-items:center;justify-content:center;gap:6px;font-weight:700;font-size:12px}
.card{position:absolute;left:656px;top:158px;width:359px;height:356px;border:1.5px solid var(--card-edge);border-radius:20px;background:radial-gradient(ellipse at 20% 100%,rgba(20,120,115,.55) 0%,rgba(11,18,19,.95) 55%),var(--card)}
.tabs{position:absolute;top:31px;left:54px;display:flex;gap:3px}
.tab{width:81px;height:24px;border-radius:3px;background:var(--tab);border:1px solid #2b3133;font-size:9px;font-weight:700;display:flex;align-items:center;justify-content:center}
.tab.active{background:var(--pill);border-color:var(--pill-edge)}
.apy{position:absolute;top:74px;width:100%;text-align:center;font-size:11px}
.apy b{color:var(--teal);font-weight:500}
.field{position:absolute;left:30px;width:296px;height:42px;border:1px solid var(--field-edge);border-radius:6px;background:var(--field)}
.pill{position:absolute;left:5px;top:5px;width:112px;height:31px;border-radius:3px;background:var(--pill);border:1px solid var(--pill-edge);display:flex;align-items:center;justify-content:center;gap:8px;font-weight:700;font-size:12px}
.token{width:20px;height:20px;border-radius:50%;background:#0c0f10;border:1.5px solid #2a3032}
.token.q{background:#f3605a;border-color:#fff}
.amount{position:absolute;right:20px;top:11px;font-size:16px}
.meta{position:absolute;left:30px;width:296px;display:flex;justify-content:space-between;font-size:7.5px;color:var(--muted)}
.meta u{margin-left:3px}
.cta{position:absolute;left:30px;top:266px;width:296px;height:43px;border-radius:6px;background:var(--orange);font-weight:700;font-size:16px;display:flex;align-items:center;justify-content:center;letter-spacing:.3px}
.footer{position:absolute;left:0;top:685px;width:1200px;height:35px;border-top:1px solid #1e2a28;background:rgba(6,17,15,.9);font-size:8px;display:flex;align-items:center;padding:0 184px}
.foot-links{position:absolute;left:588px;display:flex;gap:7px}
.foot-links i{font-style:normal;color:#7d8b88}
.socials{margin-left:auto;display:flex;gap:10px;font-weight:600}
</style>
</head>
<body>
<div class="page">
  <div class="announce">Quillo Points system is live! Earn when using quilloTNX in Defi. <a href="#">Learn how it works</a></div>

  <header class="nav">
    <div class="brand"><span class="brand-dot"></span>QuilloStake</div>
    <nav class="nav-links">
      <span>Home</span><span>Validators</span><span>Points</span><span>Docs</span>
      <span class="nav-btn">Connect Wallet</span>
    </nav>
  </header>

  <div class="moon" role="img" aria-label="Large teal-tinted moon surface rising from the bottom of the page"></div>

  <section class="hero">
    <h1>Liquid Staking on<br><span>Tarnex</span></h1>
    <p>Quillo Stake Pool offers non-custodial staking. Stake your TNX to receive a liquid staking token, quilloTNX, that you can use in Defi on Tarnex. When you hold and use quilloTNX you also earn points.</p>
    <div class="hero-btn">What is liquid staking?
      <svg width="12" height="12" viewBox="0 0 12 12" fill="none" stroke="#fff" stroke-width="1.6" stroke-linecap="round" stroke-linejoin="round"><path d="M1.5 6h9M6.5 2l4 4-4 4"/></svg>
    </div>
  </section>

  <section class="card">
    <div class="tabs">
      <div class="tab active">Stake</div><div class="tab">Unstake</div><div class="tab">Referral</div>
    </div>
    <div class="apy">Current APY: <b>8.29%</b> across 60 validators</div>

    <div class="field" style="top:111px">
      <div class="pill"><span class="token"></span>TNX</div>
      <div class="amount">0</div>
    </div>
    <div class="meta" style="top:160px"><span>balance: 0 TNX</span><span><u>max</u><u>half</u></span></div>

    <div class="field" style="top:189px">
      <div class="pill"><span class="token q"></span>quilloTNX</div>
      <div class="amount">0</div>
    </div>
    <div class="meta" style="top:238px"><span>balance: 0 quilloTNX</span><span>1 quilloTNX = 1.01805 TNX</span></div>

    <div class="cta">CONNECT WALLET</div>
    <div class="meta" style="top:316px"><span>Priority fees</span><span>Yes</span></div>
  </section>

  <footer class="footer">
    <span>© 2024 Quillo Stake. All Rights Reserved.</span>
    <div class="foot-links"><span>defi</span><i>|</i><span>docs</span><i>|</i><span>validators</span><i>|</i><span>points</span></div>
    <div class="socials"><span>Chatterbox</span><span>Postline</span></div>
  </footer>
</div>
</body>
</html>
```